Willowmere Paws Gala Sponsor & Stallholder Leaflet Design

Willowmere Paws Gala is the updated and refreshed version of the Brackenfield Pup Fair (See www.brackenfieldpupfair.co.uk).
Under new management, we need a leaflet designed to promote the event to potential stallholders and sponsors.
Willowmere Paws Gala is a fun day out for dogs and their human companions, with a range of activities for both.
As this is an outdoor event, we would like this theme in the leaflet.
It is being held in the grounds of Ashcombe Hall - http://www.ashcombehall.com
Attached is the required copy.
Note:
Leaflet format of DL/6 page is preferred, but will accept A5/4page
I will require the final work in InDesign format
Target Market(s)
Dog owners and lovers
Industry/Entity Type
Event
Look and feel

```html
<!DOCTYPE html>
<html lang="en">
<head>
<meta charset="utf-8">
<title>Willowmere Paws Gala – Leaflet</title>
<link rel="stylesheet" href="https://fonts.googleapis.com/css2?family=Oswald:wght@300;400&display=swap">
<style>
  :root {
    --paper: #ffffff;
    --brand-orange: #e8501c;
    --label-dark: rgba(58, 52, 44, 0.78);
    --panel-light: rgba(255, 255, 255, 0.22);
    --ink-light: #ffffff;
    --sky: #f4f6ee;
    --grass-light: #9fc25a;
    --grass-mid: #5f9a2c;
    --grass-deep: #3c7420;
  }
  * { margin: 0; padding: 0; box-sizing: border-box; }
  html, body { width: 1200px; height: 2541px; overflow: hidden; background: var(--paper); }
  .leaflet {
    position: relative;
    width: 1200px;
    height: 2541px;
    overflow: hidden;
    font-family: "Oswald", sans-serif;
    font-weight: 300;
    color: var(--ink-light);
    background: var(--paper);
  }
  .field-photo {
    position: absolute;
    left: 0; top: 520px;
    width: 1200px; height: 2021px;
    background:
      radial-gradient(ellipse 520px 420px at 1050px 240px, rgba(255,255,240,0.9), rgba(255,255,240,0) 70%),
      linear-gradient(180deg, var(--paper) 0%, var(--sky) 7%, #d9e6b8 14%, var(--grass-light) 24%, var(--grass-mid) 55%, var(--grass-deep) 100%);
  }
  .brand {
    position: absolute;
    left: 44px; top: 170px;
    display: flex; align-items: center; gap: 34px;
  }
  .brand-name {
    font-weight: 400;
    font-size: 128px;
    line-height: 1;
    color: var(--brand-orange);
    letter-spacing: -1px;
  }
  .brand-dot {
    width: 150px; height: 150px;
    border-radius: 50%;
    background: #111111;
  }
  .label {
    position: absolute;
    left: 21px;
    height: 100px;
    padding: 0 24px;
    background: var(--label-dark);
    font-size: 66px;
    line-height: 100px;
    font-variant: small-caps;
    text-transform: lowercase;
    letter-spacing: 1px;
  }
  .panel {
    position: absolute;
    left: 21px;
    background: var(--panel-light);
    font-variant: small-caps;
    letter-spacing: 1px;
  }
  .label-what { top: 872px; }
  .panel-what {
    top: 990px; width: 770px;
    padding: 18px 24px 26px;
    font-size: 64px; line-height: 86px;
  }
  .label-when { top: 1492px; }
  .panel-when {
    top: 1620px; padding: 0 24px;
    height: 130px; line-height: 130px;
    font-size: 72px;
    background: var(--label-dark);
    background: rgba(255,255,255,0.18);
  }
  .label-where { top: 1848px; }
  .panel-where {
    top: 1990px; padding: 0 24px;
    height: 132px; line-height: 132px;
    font-size: 66px;
  }
  .site-link {
    position: absolute;
    left: 0; bottom: 20px;
    padding: 14px 22px;
    background: rgba(40, 36, 30, 0.45);
    font-size: 40px;
    letter-spacing: 2px;
    text-transform: uppercase;
  }
</style>
</head>
<body>
<main class="leaflet">
  <div class="field-photo" role="img" aria-label="Photograph of a long-haired collie dog running across a sunlit green grass field toward the viewer, bright sun flare at top right"></div>

  <header class="brand">
    <span class="brand-name">Willowmere Paws Gala</span>
    <span class="brand-dot" aria-hidden="true"></span>
  </header>

  <h2 class="label label-what">What?</h2>
  <p class="panel panel-what">Willowmere Paws Gala is a fun day out for dogs, their lovers and owners, with a range of activities for both.</p>

  <h2 class="label label-when">When?</h2>
  <p class="panel panel-when">27th &amp; 28th July 2013</p>

  <h2 class="label label-where">Where?</h2>
  <p class="panel panel-where">Ashcombe Hall, North Wealdshire</p>

  <p class="site-link">www.willowmerepawsgala.co.uk</p>
</main>
</body>
</html>
```